New Business Card Design Project for Handyman Business

I would like to purchase a customized version of a design you have previously submitted - https://www.plimvaro.example/work/58302716
I love this design!
I am hoping you can design something similar to this for our Handyman Business.
Attached is our logo and some graphics we have used.
Here is a link to the Google Doc with the content that needs to be included, https://files.trenowick.example/sheet/q/4XRKW-7hLp2DnQv8sTc5ma-ZzoeB3kWu9YyTgp6HJ__RmwNdVcQeLbs4jfnv0ztqxhaK7M41p9ggWHe/view
Target Market(s)
Real Estate Agents, Home Owners and Property Managers
Industry/Entity Type
Construction/ Speciality Trade
Contact Information for Business Card
https://files.trenowick.example/sheet/7QpaRzN_ukoyb4cXTwLHhJe8KnuSbPjCr2QDaLy6nwod/view?mode=shared
Font styles to use
Other font styles liked:
- Ubuntu
Look and feel
Each slider illustrates characteristics of the customer's brand and the style your logo design should communicate.

```html
<!DOCTYPE html>
<html lang="en">
<head>
<meta charset="utf-8">
<title>Brindlework Business Card</title>
<link rel="stylesheet" href="https://fonts.googleapis.com/css2?family=Montserrat:wght@600;700&family=Ubuntu:wght@400;500;700&display=swap">
<style>
  :root {
    --stage: #3b3b3d;
    --brand-blue: #1a6db8;
    --back-blue: #0f5fa3;
    --brand-green: #4cb848;
    --brand-orange: #ef6b2e;
    --ink: #1e1e1e;
    --rule: #a9a9a9;
    --paper: #ffffff;
  }
  * { box-sizing: border-box; margin: 0; padding: 0; }
  html, body { width: 1200px; height: 1200px; overflow: hidden; }
  body {
    background: var(--stage);
    font-family: "Ubuntu", sans-serif;
    display: flex;
    align-items: center;
    justify-content: center;
    gap: 60px;
  }
  .card {
    width: 440px;
    height: 770px;
    border-radius: 40px;
    box-shadow: 0 6px 0 var(--brand-green), 0 18px 30px rgba(0,0,0,.35);
    display: flex;
    flex-direction: column;
    align-items: center;
    text-align: center;
  }
  .card-front { background: var(--paper); padding: 70px 40px 0; }
  .card-back { background: var(--back-blue); justify-content: center; padding: 0 34px; }

  .logo { display: flex; align-items: center; gap: 12px; }
  .logo-square { width: 34px; height: 34px; background: var(--brand-blue); }
  .logo-name { font-weight: 500; font-size: 46px; color: var(--brand-blue); letter-spacing: -0.5px; }
  .card-back .logo-square { background: var(--paper); }
  .card-back .logo-name { color: var(--paper); }
  .tagline {
    margin-top: 6px;
    font-size: 14px;
    letter-spacing: 3.5px;
    color: var(--brand-orange);
    font-weight: 500;
  }

  .portrait {
    margin-top: 30px;
    width: 214px;
    height: 214px;
    border-radius: 50%;
    border: 5px solid var(--brand-blue);
    background: radial-gradient(circle at 50% 40%, #e4c3ad 0%, #c69a82 35%, #3fa7dd 70%, #2a8fcc 100%);
  }

  .person-name {
    margin-top: 26px;
    font-family: "Montserrat", sans-serif;
    font-weight: 700;
    font-size: 34px;
    color: var(--brand-blue);
    letter-spacing: 0.5px;
  }
  .person-role { font-size: 19px; color: var(--brand-green); margin-top: 2px; letter-spacing: 0.5px; }

  .rule { width: 340px; height: 1px; background: var(--rule); margin: 16px 0; }
  .contact { color: var(--ink); line-height: 1.22; }
  .contact-phone { font-size: 26px; }
  .contact-email { font-size: 21px; }
  .contact-web { font-size: 24px; }

  .services { font-family: "Montserrat", sans-serif; font-weight: 600; font-size: 15px; line-height: 1.5; }
  .services-scope { color: var(--brand-green); }
  .services-list { color: var(--brand-blue); display: flex; align-items: center; justify-content: center; gap: 8px; }
  .marker { width: 7px; height: 7px; background: var(--brand-green); transform: rotate(45deg); display: inline-block; }

  .social { display: flex; align-items: center; gap: 12px; margin-top: 44px; }
  .social-line { width: 42px; height: 2px; background: var(--brand-green); }
  .social-dot { width: 40px; height: 40px; border-radius: 50%; border: 2px solid var(--brand-green); }
  .hashtag { margin-top: 20px; color: var(--paper); font-size: 19px; font-weight: 500; }
</style>
</head>
<body>
  <section class="card card-front">
    <div class="logo">
      <span class="logo-square"></span>
      <span class="logo-name">brindlework</span>
    </div>
    <p class="tagline">HOME CARE SPECIALISTS</p>
    <div class="portrait" role="img" aria-label="Portrait photo of the owner"></div>
    <h1 class="person-name">MARA KESSLING</h1>
    <p class="person-role">OWNER / HANDYMAN</p>
    <div class="rule"></div>
    <div class="contact">
      <p class="contact-phone">(555) 014-2287</p>
      <p class="contact-email">mara@brindlework.example</p>
      <p class="contact-web">Brindlework.example</p>
    </div>
    <div class="rule"></div>
    <div class="services">
      <p class="services-scope">COMMERCIAL AND RESIDENTIAL HANDYMAN</p>
      <p class="services-list">IMPROVE <span class="marker"></span> REPAIR <span class="marker"></span> REMODEL <span class="marker"></span> MAINTAIN</p>
    </div>
  </section>

  <section class="card card-back">
    <div class="logo">
      <span class="logo-square"></span>
      <span class="logo-name">brindlework</span>
    </div>
    <p class="tagline">HOME CARE SPECIALISTS</p>
    <div class="social" aria-label="Social media links">
      <span class="social-line"></span>
      <span class="social-dot"></span>
      <span class="social-dot"></span>
      <span class="social-dot"></span>
      <span class="social-dot"></span>
      <span class="social-line"></span>
    </div>
    <p class="hashtag">#BrindleworkHandymanServices</p>
  </section>
</body>
</html>
```